Web Design for Recruitment Agency

We need a new web design for the company who provides professional services in Labor Recruitment and Home Helpers Hire.

The sections to be covered:
1. About us
2. Philosophy
3. Services
- Labor Recruitment
* skilled workers
* unskilled workers
- Home Helpers
4. Search CV
5. Testimonials
5. Contact us

Examples:
http://www.qorvintaluae.com
http://pemlodcare.ae

The website should be clean and elegant. It should portray professionalism and attention to details.

It is important to have interactive and easy-to-navigate design with lots of pictures.

We want clients to get the right impression and be able to request a contact in case they have a requirement. We also want clients to be able to search for CVs that are already in the database. CV should be displayed as a profile card (photo and brief information about the candidate).

Logo is attached.

Target Market(s)

Local families, companies.

Industry/Entity Type

It Company

Number of Pages Required

1 page

Font styles to use
Sans Serif

Requirements
Must have
• Clean layout with pictures
Nice to have
• Dynamic, engaging website.

```html
<!DOCTYPE html>
<html lang="en">
<head>
<meta charset="utf-8">
<title>Norvale Recruitment</title>
<link href="https://fonts.googleapis.com/css2?family=Roboto:wght@300;400;500;700&family=Open+Sans:wght@400;600;700&display=swap" rel="stylesheet">
<style>
:root{
  --green:#1a8a4a;
  --green-dark:#137a3e;
  --green-band:#1e8f4e;
  --navy:#1c2a4a;
  --ink:#333a44;
  --muted:#7b838c;
  --line:#dfe3e6;
  --paper:#ffffff;
  --panel:#f2f4f5;
  --head-bg:#f4f6f5;
}
*{box-sizing:border-box;margin:0;padding:0}
html,body{width:1200px;height:2168px;overflow:hidden}
body{position:relative;background:var(--paper);font-family:"Open Sans",Arial,sans-serif;color:var(--ink);font-size:13px}
.header-band{position:absolute;left:0;top:0;width:1200px;height:140px;background:var(--head-bg)}
.green-band{position:absolute;left:0;top:140px;width:1200px;height:580px;background:linear-gradient(180deg,var(--green-band),var(--green))}
.header{position:absolute;left:100px;top:0;width:1000px;height:140px;display:flex;align-items:center;justify-content:space-between}
.brand{display:flex;align-items:center;gap:12px;font-family:"Roboto",sans-serif;font-weight:700;font-size:26px;color:var(--green)}
.brand-dot{width:46px;height:46px;border-radius:50%;background:var(--green)}
.header-contacts{display:flex;gap:40px}
.contact-item{display:flex;align-items:center;gap:12px;font-size:14px;line-height:20px}
.contact-item strong{font-weight:700;font-size:17px;color:var(--ink)}
.contact-icon{width:40px;height:40px;border-radius:50%;border:1px solid var(--line);display:flex;align-items:center;justify-content:center;background:#fff}
.nav{position:absolute;left:100px;top:160px;width:1000px;height:48px;background:#fff;display:flex;align-items:center;padding:0 0 0 12px;gap:6px;font-family:"Roboto",sans-serif;font-size:15px}
.nav a{display:block;padding:0 26px;height:48px;line-height:48px;color:var(--ink);text-decoration:none}
.nav a.active{background:var(--navy);color:#fff}
.hero{position:absolute;left:100px;top:232px;width:1000px;height:528px;background:linear-gradient(180deg,#b9d6ee 0,#dfe8ef 45%,#e8ebee 100%);overflow:hidden;box-shadow:0 6px 14px rgba(0,0,0,.18)}
.hero-photo{position:absolute;left:0;top:0;width:1000px;height:528px;background:linear-gradient(90deg,#c8d3dc 0,#3a66a8 30%,#d9dde2 50%,#2d5fa0 70%,#c8d3dc 100%);opacity:.55}
.hero-title{position:absolute;left:0;top:30px;width:1000px;text-align:center;font-family:"Roboto",sans-serif;font-weight:700;font-size:38px;color:var(--green-dark);letter-spacing:1px}
.hero-dots{position:absolute;left:0;bottom:22px;width:1000px;display:flex;justify-content:center;gap:10px}
.hero-dots span{width:12px;height:12px;border-radius:50%;background:#fff;opacity:.7}
.hero-dots span.on{background:var(--navy);opacity:1}
.section-title{font-family:"Roboto",sans-serif;font-weight:400;font-size:26px;color:var(--ink)}
.services{position:absolute;left:100px;top:790px;width:1000px}
.services .section-title{margin-bottom:20px}
.services-body{display:flex;gap:40px}
.services-intro{width:300px}
.office-photo{width:300px;height:172px;background:linear-gradient(135deg,#3b4d63,#8a98a8 60%,#c9d1da)}
.services-intro p{margin-top:14px;font-size:12px;line-height:19px;color:var(--muted)}
.service-grid{display:grid;grid-template-columns:1fr 1fr;gap:46px 40px;width:660px}
.service{display:flex;gap:20px}
.service-icon{flex:none;width:80px;height:80px;border-radius:50%;border:2px solid var(--line);display:flex;align-items:center;justify-content:center}
.service h3{font-family:"Roboto",sans-serif;font-weight:400;font-size:20px;margin:6px 0 8px}
.service p{font-size:11px;line-height:17px;color:var(--muted)}
.read-more{display:flex;align-items:center;gap:8px;margin-top:8px;font-size:12px;color:var(--ink)}
.read-more i{width:14px;height:14px;border-radius:50%;background:var(--navy);display:inline-block;position:relative}
.read-more i::after{content:"";position:absolute;left:3px;top:4.5px;width:4px;height:4px;border-top:1.5px solid #fff;border-right:1.5px solid #fff;transform:rotate(45deg)}
.search{position:absolute;left:0;top:1180px;width:640px;height:372px;background:var(--green);padding:44px 0 0 100px;color:#fff}
.search h2{font-family:"Roboto",sans-serif;font-weight:400;font-size:30px;letter-spacing:1px;margin-bottom:28px}
.search-form{width:460px;display:grid;grid-template-columns:1fr 1fr;gap:14px 16px}
.search-form input{height:34px;border:0;padding:0 12px;font-size:11px;font-family:inherit;color:var(--muted);background:#fff}
.search-form button{grid-column:1/3;height:38px;border:0;background:var(--navy);color:#fff;font-family:"Roboto",sans-serif;font-size:14px}
.search-note{width:460px;margin-top:18px;font-size:13px;line-height:20px}
.search-note b{font-size:17px;font-weight:600}
.why{position:absolute;left:640px;top:1180px;width:560px;height:372px;background:var(--panel);padding:40px 0 0 40px}
.why .section-title{margin-bottom:22px}
.why-item{display:flex;gap:12px;margin-bottom:16px;width:420px}
.why-item svg{flex:none;margin-top:2px}
.why-item h4{font-family:"Roboto",sans-serif;font-weight:400;font-size:17px;color:var(--green-dark);margin-bottom:4px}
.why-item p{font-size:11px;line-height:16px;color:var(--muted)}
.testimonials{position:absolute;left:100px;top:1584px;width:1000px}
.testimonials .section-title{margin-bottom:24px}
.quotes{display:flex;gap:40px}
.quote{flex:1;display:flex;gap:22px;align-items:flex-start}
.quote-photo{flex:none;width:100px;height:100px;border-radius:50%;background:linear-gradient(180deg,#9aa6b2,#2f3a4a)}
.quote p{font-size:12px;line-height:18px;color:var(--muted);font-style:italic}
.quote p::before{content:"\201C";font-size:28px;color:var(--ink);vertical-align:-8px;margin-right:4px}
.stars{margin:8px 0 6px;display:flex;gap:3px}
.quote h5{font-size:13px;color:var(--green);font-weight:600}
.footer{position:absolute;left:0;top:1740px;width:1200px;height:392px;background:var(--navy);color:#c3c9d4;padding:48px 100px 0;display:flex;gap:50px}
.footer h6{font-family:"Roboto",sans-serif;font-weight:500;font-size:15px;color:#fff;margin-bottom:16px;letter-spacing:.5px}
.footer p,.footer li{font-size:11px;line-height:18px}
.footer ul{list-style:none}
.col-about{width:260px}
.col-links{width:150px}
.col-news{width:250px}
.col-news input{width:230px;height:32px;border:0;margin:14px 0 12px;padding:0 10px;font-size:11px;font-family:inherit}
.col-news button{height:28px;padding:0 14px;border:0;background:var(--green);color:#fff;font-size:11px;font-family:"Roboto",sans-serif}
.socials{display:flex;gap:6px;margin-top:10px}
.socials span{width:20px;height:20px;border-radius:50%;border:1px solid #c3c9d4}
.bottom-bar{position:absolute;left:0;top:2132px;width:1200px;height:36px;background:var(--green);color:#fff;font-size:10px;line-height:36px;text-align:center}
</style>
</head>
<body>
<div class="header-band"></div>
<div class="green-band"></div>

<header class="header">
  <div class="brand"><span class="brand-dot"></span>Norvale</div>
  <div class="header-contacts">
    <div class="contact-item">
      <span class="contact-icon"><svg width="18" height="18" viewBox="0 0 24 24"><path d="M6.6 10.8a15 15 0 0 0 6.6 6.6l2.2-2.2c.3-.3.7-.4 1-.2 1.1.4 2.3.6 3.6.6.6 0 1 .4 1 1V20c0 .6-.4 1-1 1A17 17 0 0 1 3 4c0-.6.4-1 1-1h3.5c.6 0 1 .4 1 1 0 1.3.2 2.5.6 3.6.1.3 0 .7-.2 1z" fill="#333a44"/></svg></span>
      <div><strong>Ph: (02) 5550 1846</strong><br>info@norvalerecruit.com</div>
    </div>
    <div class="contact-item">
      <span class="contact-icon"><svg width="16" height="18" viewBox="0 0 24 24"><path d="M12 2a7 7 0 0 0-7 7c0 5 7 13 7 13s7-8 7-13a7 7 0 0 0-7-7zm0 9.5A2.5 2.5 0 1 1 12 6.5a2.5 2.5 0 0 1 0 5z" fill="#333a44"/></svg></span>
      <div>148 Harlow Street<br>Brayton, QLD 4812</div>
    </div>
  </div>
</header>

<nav class="nav">
  <a class="active">Home</a><a>About us</a><a>Philosophy</a><a>Services</a><a>Search CV</a><a>Testimonials</a><a>Contact us</a>
</nav>

<section class="hero">
  <div class="hero-photo" role="img" aria-label="Group of workers in hard hats, overalls and service uniforms"></div>
  <h1 class="hero-title">NORVALE LABOUR SUPPLY</h1>
  <div class="hero-dots"><span class="on"></span><span></span><span></span><span></span></div>
</section>

<section class="services">
  <h2 class="section-title">Our Services</h2>
  <div class="services-body">
    <div class="services-intro">
      <div class="office-photo" role="img" aria-label="Businessman working at a laptop in an office"></div>
      <p>Lorem ipsum dolor sit amet, consectetur adipiscing elit, sed do eiusmod tempor incididunt ut labore et dolore magna aliqua. Ut enim ad minim veniam, quis nostrud exercitation ullamco laboris nisi ut aliquip ex ea commodo consequat duis aute irure.</p>
    </div>
    <div class="service-grid">
      <div class="service">
        <div class="service-icon"><svg width="34" height="30" viewBox="0 0 34 30"><circle cx="12" cy="8" r="6" fill="#333a44"/><path d="M1 29c0-7 5-11 11-11s11 4 11 11z" fill="#333a44"/><circle cx="24" cy="9" r="5" fill="#7b838c"/><path d="M22 18c6 0 11 3 11 10h-8c0-4-1-7-3-10z" fill="#7b838c"/></svg></div>
        <div><h3>Labor Recruitment</h3><p>Pellentesque sed dolor aliquet, viverra nulla sit amet, fringilla dolor.</p><div class="read-more">Read More <i></i></div></div>
      </div>
      <div class="service">
        <div class="service-icon"><svg width="30" height="30" viewBox="0 0 30 30"><path d="M3 15 27 3 20 27l-5-9z" fill="none" stroke="#333a44" stroke-width="2.5" stroke-linejoin="round"/><path d="M15 18 27 3" stroke="#333a44" stroke-width="2"/></svg></div>
        <div><h3>Skilled Workers</h3><p>Pellentesque sed dolor aliquet, viverra nulla sit amet, fringilla dolor.</p><div class="read-more">Read More <i></i></div></div>
      </div>
      <div class="service">
        <div class="service-icon"><svg width="30" height="30" viewBox="0 0 30 30"><rect x="3" y="13" width="6" height="14" fill="#333a44"/><path d="M11 13l6-10c2 0 3 2 2 5l-1 4h7c2 0 3 2 2 4l-3 9c-.5 1.5-1.5 2-3 2H11z" fill="none" stroke="#333a44" stroke-width="2.2" stroke-linejoin="round"/></svg></div>
        <div><h3>Unskilled Workers</h3><p>Pellentesque sed dolor aliquet, viverra nulla sit amet, fringilla dolor.</p><div class="read-more">Read More <i></i></div></div>
      </div>
      <div class="service">
        <div class="service-icon"><svg width="32" height="30" viewBox="0 0 32 30"><path d="M2 15 16 3l14 12" fill="none" stroke="#333a44" stroke-width="2.6" stroke-linejoin="round"/><path d="M6 13v15h7v-8h6v8h7V13" fill="#333a44"/></svg></div>
        <div><h3>Home Helpers</h3><p>Pellentesque sed dolor aliquet, viverra nulla sit amet, fringilla dolor.</p><div class="read-more">Read More <i></i></div></div>
      </div>
    </div>
  </div>
</section>

<section class="search">
  <h2>SEARCH CV</h2>
  <form class="search-form">
    <input placeholder="Your Name"><input placeholder="Job Title">
    <input placeholder="Experience"><input placeholder="Nationality">
    <button type="button">SEARCH CV</button>
  </form>
  <p class="search-note"><b>Important:</b> Donec tempus sed diam vitae quam sodales, sit amet augue malesuada quis adipiscing. Aliquam dolor urna.</p>
</section>

<section class="why">
  <h2 class="section-title">Why Norvale Recruitment</h2>
  <div class="why-item"><svg width="18" height="18" viewBox="0 0 18 18"><path d="M2 9l5 5 9-10" fill="none" stroke="#1a8a4a" stroke-width="2.6"/></svg><div><h4>Customer Oriented</h4><p>Lorem ipsum dolor sit amet, consectetur adipiscing elit, sed do eiusmod tempor incididunt ut labore.</p></div></div>
  <div class="why-item"><svg width="18" height="18" viewBox="0 0 18 18"><path d="M2 9l5 5 9-10" fill="none" stroke="#1a8a4a" stroke-width="2.6"/></svg><div><h4>CV Management</h4><p>Lorem ipsum dolor sit amet, consectetur adipiscing elit, sed do eiusmod tempor incididunt ut labore.</p></div></div>
  <div class="why-item"><svg width="18" height="18" viewBox="0 0 18 18"><path d="M2 9l5 5 9-10" fill="none" stroke="#1a8a4a" stroke-width="2.6"/></svg><div><h4>Job Registration</h4><p>Free job search registration.</p></div></div>
</section>

<section class="testimonials">
  <h2 class="section-title">Testimonials</h2>
  <div class="quotes">
    <div class="quote">
      <div class="quote-photo" role="img" aria-label="Portrait of a client in a business suit"></div>
      <div><p>Lorem ipsum dolor sit amet, consectetur adipiscing elit, sed do eiusmod tempor incididunt ut labore et dolore magna aliqua, quis nostrud exercitation.</p>
      <div class="stars"><svg width="80" height="14" viewBox="0 0 80 14"><g fill="#f2a81d"><path id="st" d="M7 0l2 4.5 5 .5-3.8 3.3 1.1 5L7 10.7 2.7 13.3l1.1-5L0 5l5-.5z"/><use href="#st" x="16"/><use href="#st" x="32"/><use href="#st" x="48"/></g><use href="#st" x="64" fill="#dfe3e6"/></svg></div>
      <h5>JOHN DOE</h5></div>
    </div>
    <div class="quote">
      <div class="quote-photo" role="img" aria-label="Portrait of a client in a business suit"></div>
      <div><p>Lorem ipsum dolor sit amet, consectetur adipiscing elit, sed do eiusmod tempor incididunt ut labore et dolore magna aliqua, quis nostrud exercitation.</p>
      <div class="stars"><svg width="80" height="14" viewBox="0 0 80 14"><g fill="#f2a81d"><use href="#st"/><use href="#st" x="16"/><use href="#st" x="32"/><use href="#st" x="48"/></g><use href="#st" x="64" fill="#dfe3e6"/></svg></div>
      <h5>JOHN DOE</h5></div>
    </div>
  </div>
</section>

<footer class="footer">
  <div class="col-about"><h6>NORVALE RECRUITMENT</h6><p>Lorem ipsum dolor sit amet, consectetur adipiscing elit, sed do eiusmod tempor incididunt ut labore et dolore magna aliqua. Ut enim ad minim veniam, quis nostrud exercitation ullamco laboris nisi ut aliquip ex ea commodo.</p></div>
  <div class="col-links"><h6>QUICK LINKS</h6><ul><li>HOME</li><li>ABOUT US</li><li>SERVICES</li><li>SEARCH CV</li><li>TESTIMONIALS</li><li>CONTACT US</li></ul></div>
  <div class="col-news"><h6>SIGN UP FOR NEWSLETTER</h6><p>Subscribe to receive news and job updates from our team.</p><input placeholder="Enter Name"><br><button type="button">SUBSCRIBE</button></div>
  <div class="col-contact"><h6>CONTACT US</h6><p>148 Harlow Street<br>Brayton, QLD 4812<br>Australia</p><p style="margin-top:8px">+1 (555) 014 2290<br>info@norvalerecruit.com</p><div class="socials"><span></span><span></span><span></span><span></span><span></span></div></div>
</footer>
<div class="bottom-bar">©2016 - 2017 Norvale Recruitment . All Rights Reserved</div>
</body>
</html>
```